Professional/Sleek card design for athletic apparel brand

Athletic apparel brand. Mainly focused on lifting weights/gym workouts. Logo and brand are already created. Must use brand logo and name. Creativity is welcome. Looking for a clean, modern, and sexy design.

```html
<!DOCTYPE html>
<html lang="en">
<head>
<meta charset="utf-8">
<title>Grit and Iron – Business Card</title>
<link href="https://fonts.googleapis.com/css2?family=Montserrat:wght@400;700;800&display=swap" rel="stylesheet">
<style>
  :root {
    --backdrop: #d1d4d4;
    --paper: #f4f4f4;
    --ink: #111111;
    --ink-soft: #3a3a3a;
    --rule: #6a6a6a;
  }
  * { box-sizing: border-box; margin: 0; padding: 0; }
  html, body { width: 1200px; height: 829px; overflow: hidden; }
  body {
    background: var(--backdrop);
    font-family: "Montserrat", sans-serif;
    color: var(--ink);
    position: relative;
  }
  .card {
    position: absolute;
    top: 250px;
    width: 520px;
    height: 297px;
    background: var(--paper);
    box-shadow: 0 10px 30px rgba(0,0,0,0.18);
  }
  .card--front { left: 53px; }
  .card--back { left: 627px; }

  /* front */
  .brand-block {
    position: absolute;
    left: 36px;
    top: 28px;
    width: 160px;
    border-top: 1.5px solid var(--rule);
    border-bottom: 1.5px solid var(--rule);
    padding: 5px 0;
    font-weight: 800;
    font-size: 22px;
    line-height: 1.05;
    letter-spacing: 0.5px;
    text-transform: uppercase;
  }
  .brand-block .brand-and { display: block; }
  .person {
    position: absolute;
    left: 36px;
    top: 112px;
    display: flex;
    gap: 12px;
  }
  .person__marker { width: 12px; height: 34px; background: var(--ink); }
  .person__name { font-weight: 700; font-size: 17px; letter-spacing: 0.5px; text-transform: uppercase; }
  .person__role { font-size: 11px; color: var(--ink-soft); margin-top: 2px; }
  .contacts {
    position: absolute;
    left: 48px;
    top: 172px;
    list-style: none;
    font-size: 11px;
    color: var(--ink-soft);
  }
  .contacts li { display: flex; align-items: center; gap: 7px; margin-bottom: 9px; }
  .contacts svg { width: 10px; height: 10px; fill: var(--ink); }
  .mark {
    position: absolute;
    right: 40px;
    top: 92px;
    width: 170px;
    height: 170px;
    display: flex;
    flex-direction: column;
    justify-content: center;
    align-items: flex-start;
    font-weight: 800;
    font-size: 44px;
    line-height: 1;
    text-transform: uppercase;
    letter-spacing: 1px;
  }

  /* back */
  .back-lockup {
    position: absolute;
    inset: 0;
    display: flex;
    flex-direction: column;
    align-items: center;
    justify-content: center;
    gap: 16px;
  }
  .back-lockup__square { width: 22px; height: 22px; background: var(--ink); }
  .back-lockup__name {
    font-weight: 700;
    font-size: 15px;
    letter-spacing: 10px;
    text-transform: uppercase;
  }
</style>
</head>
<body>
  <section class="card card--front" aria-label="Business card front">
    <div class="brand-block">Grit<span class="brand-and">and Iron</span></div>

    <div class="person">
      <div class="person__marker"></div>
      <div>
        <p class="person__name">Dale Harwick</p>
        <p class="person__role">CEO/Founder</p>
      </div>
    </div>

    <ul class="contacts">
      <li>
        <svg viewBox="0 0 10 10" aria-hidden="true"><path d="M2 0.5l1.8 2.2-1 1a6 6 0 0 0 3.5 3.5l1-1L9.5 8 8 9.5C4 9 1 6 0.5 2z"/></svg>
        (555) 014 2290
      </li>
      <li>
        <svg viewBox="0 0 10 10" aria-hidden="true"><path d="M0 2h10v6H0z M0 2l5 3.5L10 2" stroke="#f4f4f4" stroke-width="0.8"/></svg>
        hello@gritandiron.example
      </li>
      <li>
        <svg viewBox="0 0 10 10" aria-hidden="true"><circle cx="5" cy="5" r="4.5"/><path d="M0.5 5h9M5 0.5v9" stroke="#f4f4f4" stroke-width="0.7"/></svg>
        www.gritandiron.example
      </li>
    </ul>

    <div class="mark">
      <span>Grit</span>
      <span>and</span>
      <span>Iron</span>
    </div>
  </section>

  <section class="card card--back" aria-label="Business card back">
    <div class="back-lockup">
      <span class="back-lockup__square"></span>
      <p class="back-lockup__name">Grit and Iron</p>
    </div>
  </section>
</body>
</html>
```